Stock Broking Firm - Web Design Project

We are looking at doing a full re-design of our home page and content page and moving the majority of our content over to DNN.

Phase 1 : Website redesign www.kalvernequities.com.au

The current design is too washed out, boring and has no call to action buttons.

Solution:

KL Equities is looking for a brighter/ cleaner redesign with a few stand out call to action buttons.

• Banner with logo across the top horizontally - Bright blue logo on white background similar to www.dmq.com.au - CALL 1300 482 917 - Follow on Chirper / Facespace
• Horizontal menu bar - professional looking. - Home - About Us- Our Services - Membership - Open an Account - Become a member - Contact
• Below banner top left - large rotating banner - maybe zimbo gallery style www.tvhaldrens.com.au
• Right of rotating banner - Membership login
• Below members login - Register for Daily Market Report/ research blog - Large bright button / Name / Email / Phone / pop up??
• Below Register for daily market report - Market Indicies - RSS feed of delayed data from QNW see www.tvhaldrens.com
• Below Market indicies - KL EQUITIES - Market Tweets ( feed from our chirper page)

Below Rotating Banner -

content area

Below content area - 4 large block buttons see www.crandwickley.com.au ( hover over change colour)

Button 1 - EDUCATION - content - click here for more

Button 2 - Market Information and Research

Button 3 - Full service Broker - content brief - click here for more

Button 4 - Trade Commodities and Options

below buttons - small horizontal menu bar slightly different colour incl - Careers/ Partners / Legal Privacy FSG Site Map

Regards,
Colin Marsh

Target Market(s)

35 - 65

Industry/Entity Type

Education

Requirements
Must have
• Follow brief above - large banner, call to action buttons, F.S. Chirper, Member login etc. 4 big buttons
Nice to have
• clean looking site similar to www.dmq.com.au / not too busy. Corporate looking.
Should not have
• not too busy

```html
<!DOCTYPE html>
<html lang="en">
<head>
<meta charset="utf-8">
<title>KL Equities – Home</title>
<link rel="stylesheet" href="https://fonts.googleapis.com/css2?family=Arimo:wght@400;700&family=Open+Sans:wght@400;600&display=swap">
<style>
:root{
  --topbar:#4a4a4a;
  --nav:#1a74bb;
  --nav-dark:#13609f;
  --brand:#0d5a8f;
  --link:#1d5b93;
  --text:#333;
  --muted:#666;
  --band:#c9c9c9;
  --tile-head:#5cafe0;
  --tile-body:#e6eef8;
  --row-alt:#e4edf8;
  --button:#1777c2;
  --footer:#7d7d7d;
  --footer-line:#3c3c3c;
}
*{box-sizing:border-box;margin:0;padding:0}
html,body{width:1200px;height:1078px;overflow:hidden;background:#fff}
body{position:relative;font-family:"Arimo",Arial,sans-serif;color:var(--text);font-size:12px}
.abs{position:absolute}

/* top bar */
.topbar{left:0;top:0;width:1200px;height:32px;background:var(--topbar);color:#fff;font-size:15px}
.topbar .call{position:absolute;left:711px;top:8px}
.topbar .follow{position:absolute;left:879px;top:8px}
.social{position:absolute;top:6px;display:flex;gap:6px;font-size:11px}
.social span{display:flex;align-items:center;gap:4px}
.social i{display:inline-block;width:9px;height:9px;background:#fff}

/* people strip */
.strip{left:128px;top:40px;width:948px;height:94px}
.strip .arrow{position:absolute;top:0;width:17px;height:94px;background:#d6d8db}
.strip .arrow svg{position:absolute;top:40px;left:4px}
.card{position:absolute;top:0;width:221px;height:94px;background:linear-gradient(90deg,#f4f4f4,#e2e2e2)}
.card h4{position:absolute;left:18px;top:22px;font-size:13px;color:#444}
.card p{position:absolute;left:18px;top:46px;font-size:11.5px;line-height:19px;color:#555}
.card .portrait{position:absolute;right:4px;top:2px;width:74px;height:90px;background:linear-gradient(180deg,#cfcfcf,#9a9a9a)}

/* header */
.logo{left:195px;top:156px;font-family:"Open Sans",sans-serif;font-size:49px;color:var(--brand);font-weight:600;letter-spacing:-.5px}
.logo-mark{left:136px;top:176px;width:30px;height:30px;background:var(--brand)}
.search{left:875px;top:181px;width:200px;height:22px;border:2px solid #555;border-top-color:#888;font-size:13px;color:#444;padding:2px 9px}
.search svg{position:absolute;right:4px;top:1px}

/* nav */
.nav{left:128px;top:222px;width:948px;height:27px;background:var(--nav)}
.nav-tab{left:855px;top:209px;width:221px;height:40px;background:var(--nav);border-radius:8px 0 0 0}
.menu{left:145px;top:227px;display:flex;gap:20px;color:#fff;font-size:15.5px}
.sub{left:878px;top:222px;display:flex;gap:12px;color:#cfe6fb;font-size:11px}

/* hero */
.hero{left:128px;top:256px;width:659px;height:297px;background:linear-gradient(180deg,#7fb8ea 0%,#cfe3f5 55%,#9aa7b2 100%)}
.hero .caption{position:absolute;left:0;bottom:0;width:100%;height:41px;background:rgba(60,60,60,.6);color:#fff;font-size:11.3px;line-height:15px;padding:4px 8px}

/* login */
.login{left:834px;top:254px;width:236px;height:305px;border:1px solid #ddd;background:#fafcfe}
.login-head{left:824px;top:254px;width:255px;height:52px;background:var(--button);border-radius:10px 10px 4px 4px;color:#fff;font-family:"Open Sans",sans-serif;font-size:17px;text-align:center;padding-top:5px}
.login-head:after{content:"";position:absolute;left:0;right:0;bottom:-4px;height:10px;background:#a6dcef;border-radius:0 0 8px 8px;z-index:-1}
.login .lead{position:absolute;left:0;width:100%;top:46px;text-align:center;color:var(--link);font-size:12px}
.field{position:absolute;height:25px;border:1px solid #cfcfcf;background:#fff;font-size:12px;color:#555;padding:5px 16px}
.login .btn-login{position:absolute;left:22px;top:165px;width:78px;height:27px;border:1px solid #777;border-radius:3px;background:linear-gradient(#fafafa,#ddd);font-size:13px;padding:5px 8px 0 8px;display:flex;gap:7px}
.login .forgot{position:absolute;left:28px;top:205px;color:var(--link);font-size:12px}
.login hr{position:absolute;left:22px;top:227px;width:194px;border:0;border-top:2px solid #ccc}
.login .noacct{position:absolute;left:0;width:100%;top:248px;text-align:center;color:var(--link);font-size:12px}
.cta{position:absolute;left:21px;top:260px;width:194px;height:36px;background:var(--button);color:#fff;font-size:18px;text-align:center;line-height:36px}

/* section band */
.band{left:128px;top:568px;width:941px;height:29px;background:var(--band)}
.band-title{position:absolute;top:574px;font-size:16px;color:var(--link)}
.panel{top:597px;height:191px;border:1px solid #ccc;background:#fff}

.indices{left:128px;width:215px}
.indices table{border-collapse:collapse;width:100%;font-size:10.5px}
.indices th{text-align:left;padding:11px 4px 9px 4px;font-size:10.5px;color:#333}
.indices td{padding:5px 4px;height:23px;color:#333}
.indices tr:nth-child(even) td{background:var(--row-alt)}
.indices td.neg{color:#a01818}

.office{left:363px;width:208px}
.office .map{position:absolute;left:12px;top:8px;width:184px;height:143px;background:#1e5883;border-radius:30% 40% 45% 35%}
.office .map span{position:absolute;left:12px;top:54px;color:#fff;font-style:italic;font-weight:700;font-size:12px}
.office .postcode{position:absolute;left:11px;top:159px;width:185px;height:24px;border:1px solid #bbb;font-size:12px;color:#999;padding:4px 4px}
.office .postcode svg{position:absolute;right:7px;top:3px}

.research{left:600px;width:216px}
.research ul{list-style:none;margin-top:19px}
.research li{padding:4px 5px;font-size:10.5px;line-height:18px;color:var(--link);margin-bottom:0}
.research li:nth-child(odd){background:var(--row-alt)}
.research .more{position:absolute;right:3px;bottom:3px;font-weight:700;font-size:13px;color:var(--link)}

.register{left:852px;width:217px}
.register .field{left:4px;width:210px;height:24px;padding:5px 13px;color:#777}
.register .field.alt{background:var(--row-alt)}
.register .submit{position:absolute;left:92px;top:165px;width:117px;height:24px;background:var(--button);color:#fff;font-size:15px;text-align:center;line-height:24px;border-radius:2px}

/* tiles */
.tile{top:799px;height:147px;background:var(--tile-body)}
.tile h3{height:28px;background:var(--tile-head);color:#fff;font-weight:400;font-size:15px;text-align:center;line-height:28px}
.tile p{padding:12px 9px 0;font-size:11.8px;line-height:15.5px;color:#444}
.tile .more{position:absolute;right:8px;bottom:6px;color:var(--link);font-size:12px}

/* footer */
.footer-line{left:120px;top:968px;width:952px;height:9px;background:var(--footer-line)}
.footer{left:120px;top:977px;width:952px;height:84px;background:var(--footer);color:#fff;font-size:12px;text-align:center}
.footer .links{padding-top:16px;word-spacing:2px}
.footer .copy{padding-top:31px}
</style>
</head>
<body>

<header class="abs topbar">
  <span class="call">CALL 1300 482 917</span>
  <span class="follow">Follow on</span>
  <div class="social" style="left:962px">
    <span><i></i>Facespace</span><span><i></i>Chirper</span><span><i></i>Circlet</span>
  </div>
</header>

<section class="abs strip">
  <div class="arrow" style="left:0"><svg width="9" height="12"><path d="M8 0 0 6 8 12z" fill="#fff"/></svg></div>
  <div class="card" style="left:17px"><h4>Dane Harlow</h4><p>At last his feet<br>got down</p><div class="portrait" role="img" aria-label="Portrait photo of adviser"></div></div>
  <div class="card" style="left:250px"><h4>Tessa Quinlan</h4><p>At last his feet<br>got down</p><div class="portrait" role="img" aria-label="Portrait photo of adviser"></div></div>
  <div class="card" style="left:480px"><h4>Dane Harlow</h4><p>At last his feet<br>got down</p><div class="portrait" role="img" aria-label="Portrait photo of adviser"></div></div>
  <div class="card" style="left:710px"><h4>Marla Vestry</h4><p>At last his feet<br>got down</p><div class="portrait" role="img" aria-label="Portrait photo of adviser"></div></div>
  <div class="arrow" style="left:931px"><svg width="9" height="12"><path d="M1 0 9 6 1 12z" fill="#fff"/></svg></div>
</section>

<div class="abs logo-mark"></div>
<div class="abs logo">KL Equities</div>
<div class="abs search">Search News, Qouts
  <svg width="20" height="18"><circle cx="8" cy="7" r="5.5" fill="none" stroke="#333" stroke-width="2"/><path d="M12 11l6 6" stroke="#333" stroke-width="3"/></svg>
</div>

<div class="abs nav-tab"></div>
<nav class="abs nav"></nav>
<div class="abs menu"><span>Home</span><span>About Us</span><span>Our Services</span><span>Membership</span><span>Open an Account</span><span>Become a member</span><span>Contact</span></div>
<div class="abs sub"><span>My Alert</span><span>My Porfolio</span><span>My Account</span></div>

<section class="abs hero" role="img" aria-label="Photo of tall white residential towers against a blue sky">
  <div class="caption">•Banner with logo across the top horizontally - Bright blue logo on white background similar to www.dmq.com.au - CALL 1300 482 917 - Follow on Chirper / Facespace</div>
</section>

<div class="abs login-head">Member Login Area</div>
<section class="abs login">
  <div class="lead">LogIn and Get Access</div>
  <div class="field" style="left:12px;top:89px;width:222px">User Name</div>
  <div class="field" style="left:12px;top:135px;width:222px;padding-left:20px">Password</div>
  <div class="btn-login"><svg width="12" height="15"><path d="M3 7V4a3 3 0 016 0v3" fill="none" stroke="#2a9a2a" stroke-width="2"/><rect x="0" y="7" width="12" height="8" rx="1" fill="#2a9a2a"/></svg>Log In</div>
  <div class="forgot">Forget Password?</div>
  <hr>
  <div class="noacct">Don't have an Account?</div>
  <div class="cta">Creat Account</div>
</section>

<div class="abs band"></div>
<div class="band-title" style="left:139px">Market Summary</div>
<div class="band-title" style="left:401px">Find an Office</div>
<div class="band-title" style="left:616px">Latest Research</div>
<div class="band-title" style="left:857px">Register&nbsp; Daily Market Report</div>

<section class="abs panel indices">
  <table>
    <tr><th>Name</th><th>Value</th><th>+/-</th><th>%+/-</th></tr>
    <tr><td>Gen Ords</td><td>4,511.90</td><td class="neg">-14.70</td><td class="neg">-0.32</td></tr>
    <tr><td>KX200</td><td>4,490.74</td><td class="neg">-14.56</td><td class="neg">-0.32</td></tr>
    <tr><td>Indu</td><td>13,473.53</td><td>-</td><td>-</td></tr>
    <tr><td>HKIdx</td><td>20,919.60</td><td class="neg">-17.68</td><td class="neg">-0.08</td></tr>
    <tr><td>TechX</td><td>3,065.02</td><td>-</td><td>-</td></tr>
    <tr><td>Tokyo</td><td>8,596.23</td><td class="neg">-173.36</td><td class="neg">-1.98</td></tr>
    <tr><td>BR500</td><td>1,441.48</td><td class="neg">-14.40</td><td class="neg">-0.99</td></tr>
  </table>
</section>

<section class="abs panel office">
  <div class="map" role="img" aria-label="Map of Australia showing adviser locations"><span>Local advisers near you</span></div>
  <div class="postcode">Enter suburb or postcode...
    <svg width="18" height="18"><circle cx="7" cy="7" r="5" fill="none" stroke="#333" stroke-width="2"/><path d="M11 11l5 5" stroke="#333" stroke-width="2.5"/></svg>
  </div>
</section>

<section class="abs panel research">
  <ul>
    <li>Afternoon Market Wrap</li>
    <li style="background:none">Economic Strategy: Reconstructing Europe's banks</li>
    <li>The Daily Edge - RVO - Buy on weakness</li>
    <li style="background:none">The Daily Edge - MDX - Buy on weakness</li>
    <li>The Daily Edge - IPQ - Buy on weakness</li>
  </ul>
  <div class="more">Read more...</div>
</section>

<section class="abs panel register">
  <div class="field alt" style="top:20px">Enter Name</div>
  <div class="field" style="top:48px">e-mail Address</div>
  <div class="field alt" style="top:78px">Phone No</div>
  <div class="field" style="top:108px;padding-left:20px">Pup Ups</div>
  <div class="submit">Submit</div>
</section>

<article class="abs tile" style="left:123px;width:238px"><h3>Education</h3>
  <p>•&nbsp;&nbsp;&nbsp;&nbsp;&nbsp;&nbsp;&nbsp; Banner with logo across the top horizontally - Bright blue logo on white background similar to www.dmq.com.au - CALL 1300 482 917 - Follow on Chirper / Facespace</p><span class="more">Read More</span></article>
<article class="abs tile" style="left:364px;width:228px"><h3>Full service Broker</h3>
  <p>•&nbsp;&nbsp;&nbsp;&nbsp;&nbsp;&nbsp;&nbsp; Banner with logo across the top horizontally - Bright blue logo on white background similar to www.dmq.com.au - CALL 1300 482 917 - Follow on Chirper / Facespace</p><span class="more">Read More</span></article>
<article class="abs tile" style="left:596px;width:236px"><h3>Market Information and Research</h3>
  <p>•&nbsp;&nbsp;&nbsp;&nbsp;&nbsp;&nbsp;&nbsp; Banner with logo across the top horizontally - Bright blue logo on white background similar to www.dmq.com.au - CALL 1300 482 917 - Follow on Chirper / Facespace</p><span class="more">Read More</span></article>
<article class="abs tile" style="left:836px;width:235px"><h3>Trade Commodities and Options</h3>
  <p>•&nbsp;&nbsp;&nbsp;&nbsp;&nbsp;&nbsp;&nbsp; Banner with logo across the top horizontally - Bright blue logo on white background similar to www.dmq.com.au - CALL 1300 482 917 - Follow on Chirper / Facespace</p><span class="more">Read More</span></article>

<div class="abs footer-line"></div>
<footer class="abs footer">
  <div class="links">Terms &amp; Conditions &nbsp;|&nbsp; Financial Services Guide &nbsp;|&nbsp; Privacy Policy &nbsp;|&nbsp; Disclosure of Interests</div>
  <div class="copy">All Copyrights are reserved by KL Equities</div>
</footer>

</body>
</html>
```